Business Cards and Stationery for software company
For Software Company
Use same font as used in my logo
Eurostile-Black, Eurostile Extended #2
Bright & Fun-filled
Dorian Welby
Vice President
40627 NE 73rd Avenue Suite 815
Vancouver, WA 98682
dorianw@halvorquotes.com
www.tandrafix.com
Please keep it simple. I'm open to other fonts as long as they work with the Eurostile we currently use. Arial will be the basis for our website. Don't need to include address necessarily

```html
<!DOCTYPE html>
<html lang="en">
<head>
<meta charset="utf-8">
<title>Tandrafix Stationery</title>
<link rel="stylesheet" href="https://fonts.googleapis.com/css2?family=Michroma&family=Arimo:wght@400;700&display=swap">
<style>
  :root{
    --red:#d9232d;
    --red-soft:#f3c9cb;
    --charcoal:#3d3d3f;
    --paper:#ffffff;
    --backdrop:#ececec;
    --ink:#555555;
  }
  *{margin:0;padding:0;box-sizing:border-box}
  html,body{width:1200px;height:936px;overflow:hidden;background:var(--backdrop)}
  body{position:relative;font-family:"Arimo",Arial,sans-serif;color:var(--ink)}
  .sheet{position:absolute;background:var(--paper);box-shadow:0 2px 6px rgba(0,0,0,.12);overflow:hidden}
  .wave{position:absolute;left:0;bottom:0;width:100%}
  .url{position:absolute;left:0;width:100%;text-align:center;color:#fff;font-family:"Arimo",Arial,sans-serif;font-weight:700;letter-spacing:2px}
  .brand{font-family:"Michroma",sans-serif;color:var(--charcoal);display:flex;align-items:center;gap:8px;position:absolute;white-space:nowrap}
  .brand .dot{background:var(--red);display:inline-block;flex:none}

  /* letterhead */
  .letterhead{left:178px;top:56px;width:430px;height:564px}
  .letterhead .brand{left:22px;top:38px;font-size:15px}
  .letterhead .brand .dot{width:12px;height:12px}
  .contact{position:absolute;right:20px;top:30px;font-size:6.5px;line-height:11px;list-style:none}
  .contact li{display:flex;align-items:center;gap:5px}
  .contact li::before{content:"";width:6px;height:6px;background:var(--red);border-radius:50%}
  .faint-name{position:absolute;left:40px;top:200px;font-family:"Michroma",sans-serif;font-size:40px;color:var(--red-soft);opacity:.7}
  .letterhead .url{bottom:16px;font-size:11px}

  /* folder */
  .folder{left:633px;top:38px;width:485px;height:582px}
  .folder .brand{left:50%;top:270px;transform:translateX(-50%);font-size:34px;gap:14px}
  .folder .brand .dot{width:30px;height:30px}
  .folder .url{bottom:18px;font-size:11px}

  /* business cards */
  .card{left:43px;width:190px;height:108px}
  .card-front{top:663px}
  .card-front .brand{left:10px;top:10px;font-size:8px;gap:4px}
  .card-front .brand .dot{width:6px;height:6px}
  .card-details{position:absolute;left:74px;top:34px;font-size:5.5px;line-height:8px}
  .card-details .name{font-weight:700;color:var(--charcoal)}
  .card-back{top:787px;background:var(--charcoal)}
  .card-back .brand{left:50%;top:38px;transform:translateX(-50%);color:var(--red);font-size:14px;gap:7px}
  .card-back .brand .dot{width:11px;height:11px}
  .card-back .url{bottom:6px;font-size:5px;letter-spacing:1px;text-align:right;padding-right:12px}

  /* envelope */
  .envelope-front{left:266px;top:663px;width:448px;height:223px}
  .envelope-front .brand{left:14px;top:16px;font-size:13px;gap:6px}
  .envelope-front .brand .dot{width:10px;height:10px}
  .envelope-front .return{position:absolute;left:14px;top:40px;font-size:6px}
  .envelope-back{left:739px;top:663px;width:420px;height:228px}
  .envelope-back .url{top:22px;font-size:10px;z-index:1}
</style>
</head>
<body>

<section class="sheet letterhead">
  <div class="brand"><span class="dot"></span>TANDRAFIX</div>
  <ul class="contact">
    <li>40627 NE 73rd Avenue Suite 815</li>
    <li>Vancouver, WA 98682</li>
    <li>(360) 555-0142</li>
    <li>dorianw@halvorquotes.com</li>
    <li>www.tandrafix.com</li>
  </ul>
  <div class="faint-name" aria-hidden="true">TANDRAFIX</div>
  <svg class="wave" viewBox="0 0 430 90" height="90" preserveAspectRatio="none">
    <path d="M0 20 C120 60 260 0 430 18 L430 40 C260 22 120 70 0 40Z" fill="var(--red)"/>
    <path d="M0 46 C120 78 260 26 430 44 L430 90 L0 90Z" fill="var(--charcoal)"/>
  </svg>
  <div class="url">www.tandrafix.com</div>
</section>

<section class="sheet folder">
  <div class="brand"><span class="dot"></span>TANDRAFIX</div>
  <svg class="wave" viewBox="0 0 485 100" height="100" preserveAspectRatio="none">
    <path d="M0 22 C140 66 300 0 485 20 L485 42 C300 24 140 76 0 44Z" fill="var(--red)"/>
    <path d="M0 50 C140 84 300 28 485 48 L485 100 L0 100Z" fill="var(--charcoal)"/>
  </svg>
  <div class="url">www.tandrafix.com</div>
</section>

<section class="sheet card card-front">
  <div class="brand"><span class="dot"></span>TANDRAFIX</div>
  <div class="card-details">
    <div class="name">Dorian Welby</div>
    <div>Vice President</div>
    <div>(360) 555-0142</div>
    <div>dorianw@halvorquotes.com</div>
    <div>www.tandrafix.com</div>
  </div>
  <svg class="wave" viewBox="0 0 190 26" height="26" preserveAspectRatio="none">
    <path d="M0 6 C60 18 120 0 190 6 L190 12 C120 6 60 22 0 14Z" fill="var(--red)"/>
    <path d="M0 16 C60 24 120 8 190 14 L190 26 L0 26Z" fill="var(--charcoal)"/>
  </svg>
</section>

<section class="sheet card card-back">
  <div class="brand"><span class="dot"></span>TANDRAFIX</div>
  <div class="url">www.tandrafix.com</div>
</section>

<section class="sheet envelope-front">
  <div class="brand"><span class="dot"></span>TANDRAFIX</div>
  <div class="return">40627 NE 73rd Avenue Suite 815, Vancouver, WA 98682</div>
  <svg class="wave" viewBox="0 0 448 46" height="46" preserveAspectRatio="none">
    <path d="M0 10 C150 34 300 0 448 10 L448 20 C300 12 150 40 0 22Z" fill="var(--red)"/>
    <path d="M0 26 C150 44 300 16 448 24 L448 46 L0 46Z" fill="var(--charcoal)"/>
  </svg>
</section>

<section class="sheet envelope-back">
  <svg viewBox="0 0 420 228" width="420" height="228" preserveAspectRatio="none" style="position:absolute;left:0;top:0">
    <path d="M0 0 L420 0 L420 40 L210 120 L0 40Z" fill="var(--charcoal)"/>
    <path d="M0 40 L210 120 L420 40" fill="none" stroke="#d8d8d8" stroke-width="1"/>
  </svg>
  <div class="url">www.tandrafix.com</div>
</section>

</body>
</html>
```